South Florida Real Estate Brokerage Business

The name is DWELL VANTORO REAL ESTATE.
The company is a Real estate realty based in Miami.
Is targeted to Latin American clients.
Must express luxury, and efficiency.
Target clients for properties around 250k to a million +.
Vantoro means Royal in Latin.
Should communicate safety and knowledge of the product and transaction with a tech edge.

The web design needs to be a Social tool, with Chatterloop and other media integration of some sort. Needs to have a Show case place, a Search place (MLS listings) with maps and filters.
Needs to reflect luxury but also mixed with a social edge capable of engaging clients or transition them to communicate with the page.
Include the logo from the uploaded files, feel free to change the color or font per webdesign.
This is a Front en design, layout and graphics.
Possible future programming if approved.
I can receive Quotes for the Code part.

Target Market(s)

Spanish and English speakers living in Latin America and Canada looking for apartments and houses to buy.

Industry/Entity Type

Business

Requirements
Must have
• Search area.
Neighbourhood area.
Could be a blog or news area.
Client registration.
Social Plugin
Nice to have
• Social linking to networks.
Log in with chatterloop account.
Chatterloop Like.

```html
<!DOCTYPE html>
<html lang="en">
<head>
<meta charset="utf-8">
<title>Dwell Vantoro Real Estate</title>
<link href="https://fonts.googleapis.com/css2?family=PT+Sans:wght@400;700&family=Tenor+Sans&display=swap" rel="stylesheet">
<style>
:root{
  --gold:#b48a3c;
  --gold-light:#cfa95e;
  --gold-dark:#9c7530;
  --ink:#2a2a2a;
  --muted:#6d6d6d;
  --rule:#e3e3e3;
  --page:#f1f1f1;
  --panel:#ffffff;
  --hero-band:#2c2826;
  --footer:#262220;
  --footer-text:#8a8580;
  --field:#1c1917;
}
*{box-sizing:border-box;margin:0;padding:0}
html,body{width:1040px;height:1200px;overflow:hidden}
body{position:relative;background:var(--page);font-family:"PT Sans",Arial,sans-serif;font-size:10px;color:var(--ink);line-height:1.3}
.abs{position:absolute}
.display{font-family:"Tenor Sans",Arial,sans-serif;font-weight:400}
.accent{color:var(--gold)}
.btn{position:absolute;display:flex;align-items:center;justify-content:center;background:linear-gradient(#cba560,#a67d32);color:#fff;font-size:9px;border-radius:1px}

/* header */
.site-header{position:absolute;left:0;top:0;width:1040px;height:111px;background:#fff}
.brand{position:absolute;left:112px;top:16px;width:150px;text-align:center}
.brand-mark{width:44px;height:44px;margin:0 auto 6px;background:var(--gold)}
.brand-name{font-family:"Tenor Sans",sans-serif;font-size:12px;line-height:1.2;color:#1e1e1e;letter-spacing:.3px;border-top:1px solid #ccc;padding-top:3px;white-space:nowrap}
.brand-name small{font-size:9px;letter-spacing:.5px}
.search-label{left:284px;top:32px;font-size:10px}
.search-field{left:332px;top:24px;width:273px;height:25px;border:1px solid #ddd;padding:0 8px;display:flex;align-items:center;color:#bbb;font-style:italic;font-size:9px}
.search-btn{left:605px;top:24px;width:70px;height:25px}
.client-reg{left:700px;top:29px;font-size:9px;color:var(--muted)}
.client-reg::before{content:"";display:inline-block;border-left:4px solid var(--gold);border-top:3px solid transparent;border-bottom:3px solid transparent;margin-right:5px}
.chatter-btn{left:804px;top:24px;width:120px;height:18px;background:linear-gradient(#5270a8,#3b5790);color:#fff;font-size:9px;display:flex;align-items:center;padding-left:6px;gap:5px;border-radius:2px;white-space:nowrap}
.chatter-btn i{width:9px;height:9px;background:#fff;opacity:.85}
.nav-rule{left:279px;top:64px;width:647px;height:1px;background:var(--rule)}
.main-nav{position:absolute;left:279px;top:78px;width:647px;display:flex;justify-content:space-between;font-size:10px;color:#777;letter-spacing:.2px}
.main-nav span{padding:0 10px 8px}
.main-nav span:last-child{padding-right:0}
.main-nav .current{color:#222;border-bottom:2px solid var(--gold);padding-bottom:6px}

/* hero */
.hero-band{left:0;top:111px;width:1040px;height:306px;background:linear-gradient(90deg,#262321,#353130 50%,#262321)}
.hero-photo{left:107px;top:111px;width:819px;height:306px;background:linear-gradient(160deg,#8a7150 0%,#c9ad7a 35%,#e4d3a8 55%,#a78b5c 80%,#6e5837 100%)}
.hero-caption{left:127px;top:310px;min-width:304px;height:87px;background:rgba(35,30,26,.78);padding:16px 18px 0;font-size:19px;line-height:1.35;color:#fff;white-space:nowrap}

/* info panel */
.info-panel{left:107px;top:417px;width:819px;height:172px;background:var(--panel)}
.col-shadow{top:430px;width:1px;height:138px;background:linear-gradient(transparent,#ddd,transparent)}
.col-head{font-size:14px;border-bottom:1px solid var(--rule);padding-bottom:9px;width:221px;white-space:nowrap}
.lead{color:var(--gold)}
.copy{color:#444;font-size:10px}
.thumb{left:404px;top:472px;width:84px;height:45px;border:1px solid #ccc;background:linear-gradient(#6d8fb8,#a5b8c8 45%,#5e7a3e 60%,#3d5a2a)}
.email-field{left:683px;top:505px;width:220px;height:21px;border:1px solid #ddd;padding:0 8px;display:flex;align-items:center;color:#bbb;font-style:italic;font-size:9px}

/* neighborhoods */
.area-panel{left:107px;top:601px;width:819px;height:279px;background:var(--panel)}
.tweet-panel{left:652px;top:601px;width:274px;height:279px;background:linear-gradient(90deg,#f6f6f6,#fff 15%)}
.area-list{position:absolute;top:654px;display:flex;flex-direction:column;gap:0}
.area-list span{height:16px;padding-left:11px;position:relative;font-size:10px;white-space:nowrap}
.area-list span::before{content:"";position:absolute;left:1px;top:4px;border-left:4px solid var(--gold);border-top:3px solid transparent;border-bottom:3px solid transparent}
.area-list .hl{color:var(--gold)}
.tweet{position:absolute;left:684px;width:220px;font-size:10px;border-bottom:1px dashed #ddd;padding-bottom:6px}
.tweet small{display:block;font-size:8px;color:#999;margin-top:1px}

/* footer */
.site-footer{left:0;top:897px;width:1040px;height:303px;background:var(--footer);border-top:2px solid var(--gold)}
.foot-head{color:#fff;font-size:14px;border-bottom:1px solid #3a3532;padding-bottom:9px;white-space:nowrap}
.foot-copy{color:var(--footer-text);font-size:10px}
.social{top:1004px;width:20px;height:20px;background:#fff}
.dark-field{background:var(--field);border:1px solid #4a3c25;color:#9a8b6e;font-size:9px;padding:0 9px;display:flex;align-items:center}
.req{color:var(--gold);font-size:9px}
</style>
</head>
<body>

<header class="site-header">
  <div class="brand">
    <div class="brand-mark"></div>
    <div class="brand-name">DWELL VANTORO<br><small>REAL ESTATE</small></div>
  </div>
  <div class="abs search-label">SEARCH</div>
  <div class="abs search-field">Search keyword, location, rental or neighborhood area</div>
  <div class="btn search-btn">SEARCH</div>
  <div class="abs client-reg">Client Registration</div>
  <div class="abs chatter-btn"><i></i>Sign in with Chatterloop</div>
  <div class="abs nav-rule"></div>
  <nav class="main-nav">
    <span class="current">HOME</span><span>MIAMI CONDOS</span><span>NEIGHBORHOOD</span><span>BLOG</span><span>SEARCH</span><span>RENTALS</span><span>MAP SEARCH</span><span>CONTACT</span>
  </nav>
</header>

<div class="abs hero-band"></div>
<div class="abs hero-photo" role="img" aria-label="Sunlit luxury bedroom with draped windows, patterned armchair and a bed overlooking a forest"></div>
<div class="abs hero-caption display">South Florida’s Premier Luxury<br><span class="accent">Real Estate</span></div>

<section class="abs info-panel"></section>
<div class="abs col-shadow" style="left:370px"></div>
<div class="abs col-shadow" style="left:650px"></div>

<div class="abs" style="left:127px;top:435px">
  <h2 class="col-head display">Home Vantoro <span class="accent">News</span></h2>
  <p class="lead" style="margin-top:12px">Lorem ipsum dolor sit amet, consectetuer</p>
  <p class="copy">Adipiscing elit, sed diam nonummy nibh euismod<br>tincidunt ut laoreet dolore magna</p>
</div>
<div class="btn" style="left:130px;top:532px;width:68px;height:20px">Readmore</div>

<div class="abs" style="left:402px;top:435px">
  <h2 class="col-head display">Home Vantoro <span class="accent">Real Estate</span></h2>
</div>
<div class="abs thumb" role="img" aria-label="White two-storey house behind trees"></div>
<div class="btn" style="left:403px;top:526px;width:86px;height:20px">Search Listings</div>
<div class="abs" style="left:501px;top:472px;width:130px">
  <p class="lead">Lorem ipsum dolor sit amet consectetuer</p>
  <p class="copy">Adipiscing elit, sed diam nonummy nibh euismod tincidunt ut laoreet dolore magna</p>
</div>

<div class="abs" style="left:683px;top:435px">
  <h2 class="col-head display">Email Newsletter</h2>
  <p class="copy" style="margin-top:12px">Adipiscing elit, sed diam nonummy nibh euismod<br>tincidunt ut laoreet dolore magna</p>
</div>
<div class="abs email-field">Your email here</div>
<div class="btn" style="left:685px;top:536px;width:87px;height:20px">Subscribe Now</div>

<section class="abs area-panel"></section>
<div class="abs tweet-panel"></div>

<div class="abs" style="left:127px;top:618px;width:497px;border-bottom:1px solid var(--rule);padding-bottom:8px;display:flex;justify-content:space-between;align-items:flex-end">
  <h2 class="display" style="font-size:14px">Neighborhood <span class="accent">Area</span></h2>
  <span style="font-size:10px">Sort by <span class="accent">Name</span></span>
</div>
<div class="area-list" style="left:127px"><span>Allison Islands</span><span>Atlantis</span><span>Aventura</span><span>Bal Harbour</span><span class="hl">Bay Harbor Islands</span><span>Belle Glade</span><span>Biscayne Park</span><span>Biscayne Gardens</span><span>Boca Raton</span><span>Boynton Beach</span></div>
<div class="area-list" style="left:255px"><span>Cloud Lake</span><span>Coconut Creek</span><span>Coconut Grove</span><span>Cooper City</span><span>Coral Gables</span><span>Coral Springs</span><span>Cutler Bay</span><span class="hl">Dania</span><span>Davie</span><span>Deerfield Beach</span></div>
<div class="area-list" style="left:367px"><span>Doral</span><span class="hl">Eastern Shores</span><span>El Portal</span><span>Fisher Island</span><span>Florida City</span><span>Fort Lauderdale</span><span>Fort Pierce</span><span>Golden Beach</span><span>Goulds</span><span>Green Acres</span></div>
<div class="area-list" style="left:487px"><span>Gulf Stream</span><span>Gulf View</span><span>Hallandale</span><span>Hialeah</span><span>Hialeah Gardens</span><span>Star,Palm,Hibiscus Islands</span><span>Highland Beach</span><span>Hillsboro Beach</span><span>Hobe Sound</span><span class="hl">Hollywood</span></div>

<div class="abs" style="left:127px;top:834px;width:497px;height:1px;background:var(--rule)"></div>
<div class="abs" style="left:130px;top:850px">View neighborhood area using <span class="accent">Map</span></div>
<div class="btn" style="left:557px;top:845px;width:69px;height:20px">View All</div>

<h2 class="abs display" style="left:682px;top:618px;width:221px;font-size:14px;border-bottom:1px solid var(--rule);padding-bottom:9px">Chirpwire Feed</h2>
<div class="tweet" style="top:654px"><span class="accent">@HarborlineMia</span> I posted a new photo to Chatterloop <span class="accent">http://chrp.io/Kd7wqPzA</span><small>6 minutes ago • reply</small></div>
<div class="tweet" style="top:702px"><span class="accent">@HarborlineMia</span> I posted a new photo to Chatterloop <span class="accent">http://chrp.io/Kd7wqPzA</span><small>6 minutes ago • reply</small></div>
<div class="tweet" style="top:750px"><span class="accent">@HarborlineMia</span> I posted a new photo to Chatterloop <span class="accent">http://chrp.io/Kd7wqPzA</span><small>6 minutes ago • reply</small></div>
<div class="tweet" style="top:798px;border-bottom:none"><span class="accent">@HarborlineMia</span> I posted a new photo to Chatterloop <span class="accent">http://chrp.io/Kd7wqPzA</span><small>6 minutes ago • reply</small></div>
<svg class="abs" style="left:786px;top:845px" width="8" height="5"><path d="M0 0h8L4 5z" fill="#b48a3c"/></svg>

<footer class="abs site-footer"></footer>

<div class="abs" style="left:106px;top:930px;width:240px">
  <h2 class="foot-head display" style="font-size:13px">Speak with our <span class="accent">Home Vantoro</span> Realtors</h2>
  <p class="foot-copy" style="margin-top:13px;width:222px">If you would like to speak with one of our Home Vantoro Real Estate agents immediately please call <span style="color:#fff">305-555-0148</span> and our qualified Realtors will be happy to assist you.</p>
  <p class="accent" style="margin-top:20px">Office: (305) 555-0148, Toll Free: 800-555-0172</p>
</div>

<div class="abs" style="left:370px;top:930px;width:235px">
  <h2 class="foot-head display">Connect With Us</h2>
  <p class="foot-copy" style="margin-top:13px">Lorem ipsum dolor sit amet, consectetuer adipiscing elit, sed diam nonummy nibh.</p>
</div>
<div class="abs social" style="left:375px;width:10px;background:var(--gold)"></div>
<div class="abs social" style="left:404px"></div>
<div class="abs social" style="left:444px"></div>
<div class="abs social" style="left:486px"></div>
<div class="abs social" style="left:526px;border-radius:50%"></div>
<div class="abs social" style="left:566px;border-radius:50%"></div>
<div class="abs dark-field" style="left:371px;top:1032px;width:234px;height:26px;border-color:#1c1917;color:var(--footer-text)">www.chatterloop.com/<span class="accent">dwellvantoro</span></div>
<div class="abs" style="left:374px;top:1074px;width:38px;height:16px;background:#e8ecf3;border:1px solid #9aa8c5"></div>
<div class="abs" style="left:415px;top:1075px;width:19px;height:14px;background:#fff;border:1px solid #ccc"></div>

<div class="abs" style="left:650px;top:930px;width:275px">
  <h2 class="foot-head display">Client Login</h2>
</div>
<div class="abs dark-field" style="left:652px;top:968px;width:174px;height:24px">Username</div>
<div class="abs req" style="left:836px;top:975px">* Required</div>
<div class="abs dark-field" style="left:652px;top:999px;width:174px;height:24px">Password</div>
<div class="abs req" style="left:836px;top:1006px">* Required</div>
<div class="btn" style="left:653px;top:1036px;width:69px;height:21px;font-size:11px">Login</div>
<div class="abs foot-copy" style="left:735px;top:1041px">Click <span style="color:#fff">here</span> for forgot your password</div>

<div class="abs" style="left:107px;top:1115px;width:751px;height:1px;background:#3a3532"></div>
<div class="abs" style="left:0;top:1134px;width:1006px;text-align:center;font-size:9px;color:#6f6a65">© 2012 Home Vantoro Real Estate. All Rights Reserved. <span class="accent">Listings Site Map</span></div>

</body>
</html>
```